Book cover for publishing doctoral research about various national styles of piano playing.

I need a book cover for a publication of a doctoral research with regard to styles of piano performance characteristic to various nations.

Any images or graphics are optional, typography seems most important, but please feel free to be creative.

I attach the barcode, qsr and publisher's logo in the next few days. (Logo is still being designed).

For various reasons the size of the book is not completely decided yet. Please create your design in 7" x 10", but if at all possible, I would like to ask for files of two sizes, also including 8.5" x 11" in the final submission.

I am looking for a design that looks professional, probably simple, but I am open to any suggestions.

Dear Designers,I would like to thank you all for participation and submitting so many high-quality designs.My final decision was based on the feedback I received from my professional colleagues and potential readers.I would like to wish you all the best for the future.Best wishes,Tadeusz Added Monday, December 21, 2015

Pianists, students, music professionals

Publishing

• Title: Unfolding Seven Harbour Lullabies
• Subtitle: Memories and departures
• Author: Tadeusz Jarocki
• Space for my logo on the front page and the spine.
• On the back page, please include some space for a short biography, 'barcode' and 'qsr' code.
• Please include whatever else you consider necessary.
• Would it be possible to use the same cover to a e-book edition?

```html
<!DOCTYPE html>
<html lang="en">
<head>
<meta charset="utf-8">
<title>Unfolding Seven Harbour Lullabies – Cover Spread</title>
<link href="https://fonts.googleapis.com/css2?family=Mulish:wght@400;600;700;800&family=Pinyon+Script&display=swap" rel="stylesheet">
<style>
  :root {
    --backdrop: #d3cdcd;
    --maroon: #6b3a39;
    --paper: #efedee;
    --gold: #b3a628;
    --title-grey: #666466;
    --cream: #ece0b4;
    --teal-dark: #173236;
    --teal-mid: #3d5f66;
    --rose: #8d6a62;
    --placeholder: rgba(235, 225, 222, 0.35);
  }
  * { margin: 0; padding: 0; box-sizing: border-box; }
  html, body { width: 1200px; height: 1200px; overflow: hidden; background: var(--backdrop); }
  body { position: relative; font-family: "Mulish", sans-serif; }

  .spread { position: absolute; left: 31px; top: 222px; width: 1135px; height: 758px; }

  /* back cover */
  .back-cover {
    position: absolute; left: 0; top: 0; width: 531px; height: 758px;
    background:
      radial-gradient(ellipse 60% 30% at 55% 55%, rgba(200,170,165,.55), transparent 70%),
      radial-gradient(ellipse 50% 35% at 70% 10%, rgba(120,70,60,.7), transparent 70%),
      linear-gradient(170deg, var(--teal-dark) 0%, var(--teal-mid) 30%, var(--rose) 62%, #7d5b54 100%);
  }
  .bio-box {
    position: absolute; left: 44px; top: 109px; width: 452px; height: 312px;
    background: rgba(170, 185, 190, 0.45);
    display: flex; align-items: center; justify-content: center;
  }
  .bio-box h2 { font-weight: 700; font-size: 62px; color: #4a4d4f; letter-spacing: -0.5px; }
  .code-box {
    position: absolute; background: var(--placeholder);
    display: flex; align-items: center; justify-content: center;
    color: #8b6a63; font-weight: 600; font-size: 15px;
  }
  .code-box.qsr { left: 40px; top: 665px; width: 110px; height: 79px; }
  .code-box.barcode { left: 386px; top: 680px; width: 110px; height: 56px; font-size: 13px; letter-spacing: .5px; }

  /* spine */
  .spine { position: absolute; left: 531px; top: 0; width: 76px; height: 758px; background: var(--maroon); }
  .spine-title {
    position: absolute; left: 50%; top: 658px;
    transform-origin: 0 0; transform: rotate(-90deg) translate(0, -50%);
    white-space: nowrap; color: #fff; font-size: 22px; font-weight: 700; line-height: 1;
  }
  .spine-title span { font-size: 14.5px; font-weight: 600; }
  .spine-logo {
    position: absolute; left: 7px; top: 672px; width: 62px; height: 64px;
    background: rgba(255,255,255,.3);
    display: flex; align-items: center; justify-content: center;
  }
  .spine-logo span { transform: rotate(-30deg); color: #8a6866; font-size: 22px; font-weight: 600; }

  /* front cover */
  .front-cover { position: absolute; left: 607px; top: 0; width: 528px; height: 758px; background: var(--paper); }
  .title-kicker {
    position: absolute; left: 20px; top: 44px; width: 490px;
    font-size: 25px; font-weight: 600; color: var(--title-grey);
    letter-spacing: 13.5px; white-space: nowrap;
  }
  .title-main {
    position: absolute; left: 18px; top: 76px;
    font-size: 46px; font-weight: 800; color: var(--gold); letter-spacing: .5px; white-space: nowrap;
  }
  .rule { position: absolute; left: 0; top: 132px; width: 528px; height: 3px; background: var(--maroon); }
  .cover-photo {
    position: absolute; left: 0; top: 137px; width: 528px; height: 546px;
    background:
      linear-gradient(160deg, transparent 45%, rgba(220,205,160,.75) 72%, rgba(200,180,140,.5) 100%),
      linear-gradient(200deg, #4a2e28 0%, #1d3437 30%, #15272b 60%, #2c2b24 100%);
  }
  .subtitle {
    position: absolute; left: 0; top: 170px; width: 528px; text-align: center;
    font-family: "Pinyon Script", cursive; font-size: 34px; color: #ece7d8;
  }
  .front-logo {
    position: absolute; left: 6px; top: 612px; width: 98px; height: 66px;
    background: rgba(255,255,255,.3);
    display: flex; align-items: center; justify-content: center;
    color: #8f8262; font-size: 30px; font-weight: 600;
  }
  .author-band {
    position: absolute; left: 0; top: 686px; width: 528px; height: 52px; background: var(--maroon);
    display: flex; align-items: center; justify-content: flex-end; padding-right: 16px;
  }
  .author-band p { color: var(--cream); font-size: 20px; font-weight: 700; }
</style>
</head>
<body>
  <div class="spread">
    <section class="back-cover">
      <div class="bio-box"><h2>Biography</h2></div>
      <div class="code-box qsr">qsr code</div>
      <div class="code-box barcode">barcode</div>
    </section>

    <section class="spine">
      <p class="spine-title">Unfolding Seven Harbour Lullabies - <span>Memories and departures</span></p>
      <div class="spine-logo"><span>logo</span></div>
    </section>

    <section class="front-cover">
      <p class="title-kicker">Unfolding Seven</p>
      <h1 class="title-main">HARBOUR LULLABIES</h1>
      <div class="rule"></div>
      <div class="cover-photo" role="img" aria-label="Close-up photograph of an old upright piano keyboard in warm, faded tones"></div>
      <p class="subtitle">Memories and departures</p>
      <div class="front-logo">logo</div>
      <div class="author-band"><p>Tadeusz Jarocki</p></div>
    </section>
  </div>
</body>
</html>
```